In Store Merchandising / Display Backdrops

Hello! We are in need of a graphic designer to create vinyl backdrops and mats for our product display cabinets. The Willowmere is a cannabis dispensary in Las Vegas, Nevada. Our shop appeals to tourists and we need something eye catching and fun to increase the branding of our own store while also showcasing products displayed on the shelves. The bottom shelving mats would be a size of 16.5" width x 46" length. These we need in 5 variations- edibles, accessories, concentrates, featured, naturals. Ideally we would want the font in neon writing with neon step and repeat of our logo or something similar showcasing the branding. We have 22x door panels in our display cabinets where we would want a variation of the attached rainbow smoke design or similar muted neon design of logo. The dimensions are 28" tall x 23.5" wide. The final project would include one large backdrop wall design, a mat design with 5 variations for product display shelves, and a design for a backdrop in the display cases. Would you be up for this kind of design project? If so, please let me know details including cost. Thank you for your consideration!
Target Market(s)
Men and women ages 21+ mainly tourists
Industry/Entity Type
Cannabis
Font styles to use
Other font styles liked:
- Neon sign style
Look and feel
Each slider illustrates characteristics of the customer's brand and the style your logo design should communicate.

```html
<!DOCTYPE html>
<html lang="en">
<head>
<meta charset="utf-8">
<title>The Willowmere – Accessories Shelf Backdrop</title>
<link rel="stylesheet" href="https://fonts.googleapis.com/css2?family=Poppins:wght@800&display=swap">
<style>
  :root {
    --stage: #2e2e2e;
    --lime: #c2dc78;
    --ink: #000000;
    --white: #ffffff;
    --smoke-purple: #7a1fb0;
    --smoke-magenta: #c0208a;
    --smoke-yellow: #e8d200;
    --smoke-green: #3fbf3a;
  }
  * { margin: 0; padding: 0; box-sizing: border-box; }
  html, body {
    width: 1200px;
    height: 601px;
    overflow: hidden;
    background: var(--stage);
  }
  .backdrop {
    position: absolute;
    left: 20px;
    top: 93px;
    width: 1160px;
    height: 415px;
    background: var(--ink);
    overflow: hidden;
  }
  .backdrop-art {
    position: absolute;
    inset: 0;
    width: 100%;
    height: 100%;
    display: block;
  }
  .brand-name {
    position: absolute;
    left: 580px;
    top: 136px;
    transform: translate(-50%, -50%);
    font-family: "Poppins", sans-serif;
    font-weight: 800;
    font-size: 40px;
    line-height: 1;
    color: var(--lime);
    white-space: nowrap;
    letter-spacing: 0.5px;
  }
  .category-title {
    position: absolute;
    left: 586px;
    top: 246px;
    transform: translateX(-50%);
    font-family: "Poppins", sans-serif;
    font-weight: 800;
    font-size: 98px;
    line-height: 1.1;
    letter-spacing: -2px;
    color: var(--white);
    white-space: nowrap;
  }
</style>
</head>
<body>
  <section class="backdrop">
    <svg class="backdrop-art" viewBox="0 0 2347 840" preserveAspectRatio="none" aria-hidden="false">
      <defs>
        <radialGradient id="smoke-purple" cx="0.62" cy="0.3" r="0.45">
          <stop offset="0" stop-color="var(--smoke-purple)" stop-opacity="0.95"/>
          <stop offset="0.6" stop-color="var(--smoke-purple)" stop-opacity="0.45"/>
          <stop offset="1" stop-color="var(--smoke-purple)" stop-opacity="0"/>
        </radialGradient>
        <radialGradient id="smoke-magenta" cx="0.55" cy="0.75" r="0.35">
          <stop offset="0" stop-color="var(--smoke-magenta)" stop-opacity="0.8"/>
          <stop offset="1" stop-color="var(--smoke-magenta)" stop-opacity="0"/>
        </radialGradient>
        <radialGradient id="smoke-yellow" cx="0.3" cy="0.85" r="0.2">
          <stop offset="0" stop-color="var(--smoke-yellow)" stop-opacity="0.9"/>
          <stop offset="1" stop-color="var(--smoke-yellow)" stop-opacity="0"/>
        </radialGradient>
        <radialGradient id="smoke-green" cx="0.2" cy="0.92" r="0.15">
          <stop offset="0" stop-color="var(--smoke-green)" stop-opacity="0.9"/>
          <stop offset="1" stop-color="var(--smoke-green)" stop-opacity="0"/>
        </radialGradient>
      </defs>

      <g class="smoke-field" role="img" aria-label="Rainbow coloured smoke drifting across a black background, purple at the top fading to magenta, yellow and green at the bottom left">
        <rect x="400" y="0" width="1550" height="840" fill="url(#smoke-purple)"/>
        <rect x="400" y="0" width="1550" height="840" fill="url(#smoke-magenta)"/>
        <rect x="400" y="0" width="1550" height="840" fill="url(#smoke-yellow)"/>
        <rect x="400" y="0" width="1550" height="840" fill="url(#smoke-green)"/>
      </g>

      <g class="side-panel side-panel--left">
        <polygon points="0,0 420,0 185,280 425,840 0,840" fill="var(--lime)"/>
        <polygon points="0,0 62,0 110,275 88,275 255,840 205,840 80,565 120,565 0,300" fill="var(--ink)"/>
        <polygon points="70,0 110,0 185,280 425,840 255,840 88,275 110,275" fill="var(--lime)"/>
        <polyline points="22,385 200,565 215,635" fill="none" stroke="var(--ink)" stroke-width="5"/>
      </g>

      <g class="side-panel side-panel--right" transform="translate(2347,0) scale(-1,1)">
        <polygon points="0,0 420,0 185,280 425,840 0,840" fill="var(--lime)"/>
        <polygon points="0,0 62,0 110,275 88,275 255,840 205,840 80,565 120,565 0,300" fill="var(--ink)"/>
        <polygon points="70,0 110,0 185,280 425,840 255,840 88,275 110,275" fill="var(--lime)"/>
        <polyline points="22,385 200,565 215,635" fill="none" stroke="var(--ink)" stroke-width="5"/>
      </g>
    </svg>

    <p class="brand-name">The Willowmere</p>
    <h1 class="category-title">ACCESSORIES</h1>
  </section>
</body>
</html>
```